Website: Check-and-Settle by Clear RTM

We have a basic design concept. We would like the winning designer to clean it up and create an attractive web site for the business.

The website will have about 6 pages. We have the textual content for these pages attached. I have uploaded the basic layout of the home page in basic design wireframe. I have also uploaded a conceptual wireframe outlining the different pages on the site, and their content.

Important aspects:
This is a financial company, and the design needs to convey: stability, security, trust, and simplicity.
This is a business to business solution and we need it to appeal to business community not general consumers.

Here is a website from one of our competitors: https://www.quillmarrow.com/payment-solutions/
But we are looking for something a little classier but still maintaining industry norms.

Color and styling guide uploaded and logo uploaded

Target Market(s)

Banks and Businesses

Industry/Entity Type

Financial

Coding

Coded - Design and coding required

Font styles to use
Other font styles liked:
• Monserat

Colors
0054AA
0677BA
7BADD7
CADEEF
E8F1F8

Requirements
Must have
• Crisp look, convey stability and security
Should not have
• Consumer related materials. Strictly business to business.

```html
<!DOCTYPE html>
<html lang="en">
<head>
<meta charset="utf-8">
<title>Check-and-Settle by Clear RTM</title>
<link href="https://fonts.googleapis.com/css2?family=Poppins:wght@400;500;600;700&family=Montserrat:wght@400;500;600&display=swap" rel="stylesheet">
<style>
:root{
  --brand:#0054AA;
  --brand-dark:#0a3d9c;
  --accent:#0677BA;
  --sky:#7BADD7;
  --mist:#CADEEF;
  --ice:#E8F1F8;
  --ink:#1d1d1f;
  --muted:#555;
  --gray:#f3f3f3;
  --white:#fff;
}
*{box-sizing:border-box;margin:0;padding:0}
html,body{width:1200px;height:4532px;overflow:hidden}
body{font-family:"Poppins",sans-serif;color:var(--ink);background:var(--white);position:relative}
.abs{position:absolute}
.btn{position:absolute;display:flex;align-items:center;justify-content:center;gap:14px;font:600 19px "Poppins",sans-serif;border-radius:8px;height:64px;text-transform:uppercase}
.btn svg{width:22px;height:22px}
.btn-blue{background:var(--brand);color:var(--white)}
.btn-white{background:var(--white);color:var(--brand)}
.eyebrow{font:500 19px "Poppins",sans-serif;color:#555;text-transform:uppercase;display:flex;align-items:center;gap:10px}
.eyebrow .rule{display:inline-block;width:58px;height:2px;background:#666}
.h2{font:600 52px/62px "Poppins",sans-serif;color:var(--brand)}
.copy{font:400 16px/27px "Poppins",sans-serif;color:var(--ink)}

/* top bar */
.topbar{top:0;left:0;width:1200px;height:40px;background:var(--brand-dark);color:var(--white);font-size:13px}
.topbar .phone{left:68px;top:11px;display:flex;gap:10px;align-items:center}
.topbar .links{left:914px;top:12px;font-size:11px}
.topbar .login{left:1057px;top:9px;width:78px;height:22px;background:#0b2f7e;border-radius:3px;font-size:11px;display:flex;align-items:center;justify-content:center}
/* nav */
.nav{top:40px;left:0;width:1200px;height:80px;background:var(--white);box-shadow:0 2px 6px rgba(0,0,0,.08);z-index:2}
.logo{left:68px;top:20px;display:flex;align-items:center;gap:10px;font:700 32px "Poppins",sans-serif;color:var(--brand)}
.logo .dot{width:34px;height:34px;border-radius:50%;background:var(--brand)}
.menu{right:66px;top:30px;display:flex;gap:34px;font:400 13px "Poppins",sans-serif;color:#333}
.menu .on{color:var(--brand)}
/* hero */
.hero{top:120px;left:0;width:1200px;height:748px;background:linear-gradient(100deg,#08245e 0%,#0a3a8f 40%,#1f63c9 75%,#4a8fe3 100%)}
.hero-title{left:64px;top:190px;font:600 70px/74px "Poppins",sans-serif;color:var(--white)}
.hero-copy{left:67px;top:352px;width:560px;font:400 17px/32px "Poppins",sans-serif;color:var(--white);text-align:justify}
/* verify */
.verify{top:868px;left:0;width:1200px;height:870px}
.center{left:0;width:1200px;text-align:center;justify-content:center}
.features{left:68px;top:462px;width:1066px;height:198px;background:var(--brand);border-radius:16px}
.feat{position:absolute;display:flex;align-items:center;gap:16px;color:var(--white);font:500 17px "Poppins",sans-serif}
.feat svg{width:26px;height:26px}
/* industries */
.industries{top:1738px;left:0;width:1200px;height:742px;background:var(--gray)}
.ind{position:absolute;top:330px;width:200px;margin-left:-100px;text-align:center;font:500 20px/24px "Poppins",sans-serif}
.ind .ring{width:122px;height:122px;margin:0 auto 24px;border-radius:50%;border:2px dotted var(--brand);display:flex;align-items:center;justify-content:center}
.ind .disc{width:100px;height:100px;border-radius:50%;background:var(--brand);display:flex;align-items:center;justify-content:center}
.ind svg{width:44px;height:44px}
/* about */
.about{top:2480px;left:0;width:1200px;height:845px}
.about-title{left:66px;top:206px;width:640px;font:600 47px/62px "Poppins",sans-serif;letter-spacing:-0.5px;color:var(--brand)}
.card{left:686px;width:409px;height:287px;border:2px solid #ddd;border-radius:22px;background:var(--gray)}
.card .name{left:42px;top:36px;font:600 30px "Poppins",sans-serif;color:var(--brand)}
.card .role{left:42px;top:78px;font:400 17px "Poppins",sans-serif;color:#333}
.card .desc{left:42px;top:118px;width:230px;font:600 15px/23px "Poppins",sans-serif;color:#222}
.card .social{left:42px;top:200px;width:50px;height:50px;border-radius:50%;background:var(--brand)}
.card .photo{left:290px;top:50px;width:186px;height:186px;border-radius:50%;border:6px solid var(--white);background:radial-gradient(circle at 50% 40%,#d9c3ae,#8f9aa6 70%);box-shadow:0 2px 8px rgba(0,0,0,.1)}
/* partner */
.partner{top:3325px;left:0;width:1200px;height:260px;background:var(--brand)}
/* contact */
.contact{top:3585px;left:0;width:1200px;height:616px}
.field{position:absolute;background:var(--white);box-shadow:0 1px 6px rgba(0,0,0,.12);font:400 11px "Montserrat",sans-serif;color:#999;padding:12px 18px}
/* footer */
.footer{top:4201px;left:0;width:1200px;height:331px;background:var(--brand);color:var(--white)}
.footer .rule-line{left:70px;width:1064px;height:1px;background:rgba(255,255,255,.6)}
.fmenu{top:224px;left:0;width:1200px;display:flex;justify-content:center;gap:52px;font:400 13px "Poppins",sans-serif}
</style>
</head>
<body>

<header class="abs topbar">
  <div class="abs phone"><svg width="16" height="16" viewBox="0 0 24 24" fill="none" stroke="#fff" stroke-width="2"><path d="M5 3h4l2 5-3 2a12 12 0 0 0 6 6l2-3 5 2v4a2 2 0 0 1-2 2A17 17 0 0 1 3 5a2 2 0 0 1 2-2z"/></svg>+1 555.010.0199</div>
  <div class="abs links">SIGN-UP | SUPPORT</div>
  <div class="abs login">LOG IN</div>
</header>

<nav class="abs nav">
  <div class="abs logo"><span class="dot"></span>CLEAR RTM</div>
  <div class="abs menu"><span class="on">▪ HOME</span><span>CHECK-AND-SETTLE</span><span>PARTNERSHIPS</span><span>INDUSTRIES</span><span>ABOUT</span><span>INDUSTRIES</span><span>CONTACT</span></div>
</nav>

<section class="abs hero" role="img" aria-label="Businessman holding a phone in front of a glowing digital security padlock and circuit display">
  <h1 class="abs hero-title">Embedded<br>Payments Today</h1>
  <p class="abs hero-copy">Check-and-Settle helps avoid fraud through modern, more secure payments and better recipient verification. Supporting payment choice includes methods that are immediate and ones that can be scheduled. All recipient information is maintained by the Check-and-Settle platform.</p>
  <a class="btn btn-white" style="left:70px;top:543px;width:204px">Learn more <svg viewBox="0 0 24 24" fill="none" stroke="currentColor" stroke-width="2"><path d="M4 12h14M12 6l6 6-6 6"/></svg></a>
  <a class="btn btn-blue" style="left:289px;top:543px;width:204px;background:#1465e0">Sign-up <svg viewBox="0 0 24 24" fill="none" stroke="currentColor" stroke-width="2"><path d="M4 12h14M12 6l6 6-6 6"/></svg></a>
</section>

<section class="abs verify">
  <div class="abs eyebrow center" style="top:100px"><span class="rule"></span>Check-and-Settle<span class="rule"></span></div>
  <h2 class="abs h2 center" style="top:140px">Paying By Check Isn’t Easier<br>And Definitely Not Safe</h2>
  <p class="abs copy" style="left:145px;top:308px;width:910px;text-align:center">Avoid fraud by not paying with checks. Checks are expensive and a fraud target because they are easily lost, stolen, or modified. Modern electronic payments enable more remittance information than a check which travels along with the payment.</p>
  <p class="abs center" style="top:408px;display:block;font:600 19px Poppins,sans-serif;color:var(--brand)">Electronic payments through Check-and-Settle offer:</p>
  <div class="abs features">
    <div class="feat" style="left:73px;top:48px"><svg viewBox="0 0 24 24" fill="none" stroke="#fff" stroke-width="2"><circle cx="12" cy="12" r="10"/><path d="M7 12l3 3 7-7"/></svg>Verify Recipients</div>
    <div class="feat" style="left:73px;top:84px"><svg viewBox="0 0 24 24" fill="none" stroke="#fff" stroke-width="2"><circle cx="12" cy="12" r="10"/><path d="M7 12l3 3 7-7"/></svg>Automate Recurring Payments</div>
    <div class="feat" style="left:73px;top:120px"><svg viewBox="0 0 24 24" fill="none" stroke="#fff" stroke-width="2"><circle cx="12" cy="12" r="10"/><path d="M7 12l3 3 7-7"/></svg>Enterprise-class instant payouts</div>
    <div class="feat" style="left:458px;top:48px"><svg viewBox="0 0 24 24" fill="none" stroke="#fff" stroke-width="2"><circle cx="12" cy="12" r="10"/><path d="M7 12l3 3 7-7"/></svg>Lower Payout Fraud</div>
    <div class="feat" style="left:458px;top:84px"><svg viewBox="0 0 24 24" fill="none" stroke="#fff" stroke-width="2"><circle cx="12" cy="12" r="10"/><path d="M7 12l3 3 7-7"/></svg>Just in time Funding</div>
    <div class="feat" style="left:458px;top:120px"><svg viewBox="0 0 24 24" fill="none" stroke="#fff" stroke-width="2"><circle cx="12" cy="12" r="10"/><path d="M7 12l3 3 7-7"/></svg>Lower Managing Expenses</div>
    <div class="feat" style="left:780px;top:48px"><svg viewBox="0 0 24 24" fill="none" stroke="#fff" stroke-width="2"><circle cx="12" cy="12" r="10"/><path d="M7 12l3 3 7-7"/></svg>Embed Payments</div>
    <div class="feat" style="left:780px;top:84px"><svg viewBox="0 0 24 24" fill="none" stroke="#fff" stroke-width="2"><circle cx="12" cy="12" r="10"/><path d="M7 12l3 3 7-7"/></svg>Schedule Payments</div>
    <div class="feat" style="left:780px;top:120px"><svg viewBox="0 0 24 24" fill="none" stroke="#fff" stroke-width="2"><circle cx="12" cy="12" r="10"/><path d="M7 12l3 3 7-7"/></svg>Increase Cash Flow</div>
  </div>
  <a class="btn btn-blue" style="left:498px;top:702px;width:204px">Learn more <svg viewBox="0 0 24 24" fill="none" stroke="currentColor" stroke-width="2"><path d="M4 12h14M12 6l6 6-6 6"/></svg></a>
</section>

<section class="abs industries">
  <div class="abs eyebrow center" style="top:92px"><span class="rule"></span>Industries<span class="rule"></span></div>
  <h2 class="abs h2 center" style="top:132px;display:block">Innovation Centered – Industry Focused</h2>
  <p class="abs copy" style="left:145px;top:236px;width:910px;text-align:center">Check-and-Settle focuses on integration into the systems that run your business today. We bring the payment function directly into your workflow.</p>
  <div class="ind" style="left:137px"><div class="ring"><div class="disc"><svg viewBox="0 0 24 24" fill="#fff"><path d="M2 20V9l6 4V9l6 4V4h4v16z"/></svg></div></div>Factoring</div>
  <div class="ind" style="left:320px"><div class="ring"><div class="disc"><svg viewBox="0 0 24 24" fill="none" stroke="#fff" stroke-width="2"><rect x="2" y="5" width="20" height="14" rx="2"/><path d="M14 10h5M14 14h5M9 9H7a1.5 1.5 0 0 0 0 3h1a1.5 1.5 0 0 1 0 3H6"/></svg></div></div>HR/Payroll</div>
  <div class="ind" style="left:507px"><div class="ring"><div class="disc"><svg viewBox="0 0 24 24" fill="#fff"><rect x="4" y="2" width="16" height="10" rx="1"/><rect x="8" y="12" width="5" height="10" rx="1"/></svg></div></div>ISO Commission<br>Payments</div>
  <div class="ind" style="left:708px"><div class="ring"><div class="disc"><svg viewBox="0 0 24 24" fill="#fff"><path d="M5 6h7l2 5h6v5H3v-5h2z"/><circle cx="7" cy="17" r="3"/><circle cx="18" cy="18" r="2"/></svg></div></div>Farm<br>Management</div>
  <div class="ind" style="left:890px"><div class="ring"><div class="disc"><svg viewBox="0 0 24 24" fill="#fff"><path d="M6 9a6 6 0 0 1 12 0z"/><circle cx="12" cy="12" r="3"/><circle cx="12" cy="19" r="4"/></svg></div></div>Contractor<br>Payment</div>
  <div class="ind" style="left:1074px"><div class="ring"><div class="disc"><svg viewBox="0 0 24 24" fill="#fff"><path d="M2 5h2v8h18v6h-2v-3H4v3H2z"/><circle cx="8" cy="10" r="2"/><rect x="11" y="8" width="10" height="4" rx="1"/></svg></div></div>Factoring</div>
  <a class="btn btn-blue" style="left:498px;top:573px;width:204px">Learn more <svg viewBox="0 0 24 24" fill="none" stroke="currentColor" stroke-width="2"><path d="M4 12h14M12 6l6 6-6 6"/></svg></a>
</section>

<section class="abs about">
  <div class="abs eyebrow" style="left:70px;top:168px">About us<span class="rule"></span></div>
  <h2 class="abs about-title">Decades of experience in payments, operations, communications, and security</h2>
  <p class="abs copy" style="left:67px;top:500px;width:500px">Our passion is to reduce fraud while providing enterprise class, industry-based solutions for all sized businesses.</p>
  <a class="btn btn-blue" style="left:70px;top:605px;width:204px">Learn more <svg viewBox="0 0 24 24" fill="none" stroke="currentColor" stroke-width="2"><path d="M4 12h14M12 6l6 6-6 6"/></svg></a>
  <div class="abs card" style="top:121px">
    <div class="abs name">Daniel Reyes</div>
    <div class="abs role">Founder, CEO</div>
    <div class="abs desc">Serial entrepreneur focused on development, security, communications</div>
    <div class="abs social"></div>
    <div class="abs photo" role="img" aria-label="Portrait of the founder"></div>
  </div>
  <div class="abs card" style="top:436px">
    <div class="abs name">Marcus Bell</div>
    <div class="abs role">Payments Advisor, CRO</div>
    <div class="abs desc">Strategic channel development and go-to-market expert</div>
    <div class="abs social"></div>
    <div class="abs photo" role="img" aria-label="Portrait of the payments advisor"></div>
  </div>
</section>

<section class="abs partner">
  <div class="abs eyebrow" style="left:135px;top:80px;color:#fff">Clear RTM<span class="rule" style="background:#fff"></span></div>
  <h2 class="abs" style="left:135px;top:115px;font:600 52px Poppins,sans-serif;color:#fff">Why Partner With Us?</h2>
  <a class="btn btn-white" style="left:831px;top:103px;width:204px">Learn more <svg viewBox="0 0 24 24" fill="none" stroke="currentColor" stroke-width="2"><path d="M4 12h14M12 6l6 6-6 6"/></svg></a>
</section>

<section class="abs contact">
  <div class="abs eyebrow" style="left:102px;top:118px">Contact us<span class="rule"></span></div>
  <h2 class="abs h2" style="left:100px;top:158px">Let’s collaborate on<br>your innovative ideas</h2>
  <p class="abs copy" style="left:104px;top:308px;width:480px;text-align:justify">We would enjoy hearing from you. Drop us a question, comment, or schedule time to pick our brains.</p>
  <a class="btn btn-blue" style="left:106px;top:424px;width:258px">Schedule today <svg viewBox="0 0 24 24" fill="none" stroke="currentColor" stroke-width="2"><path d="M4 12h14M12 6l6 6-6 6"/></svg></a>
  <div class="field" style="left:686px;top:144px;width:198px;height:39px">First Name:</div>
  <div class="field" style="left:903px;top:144px;width:197px;height:39px">Last Name:</div>
  <div class="field" style="left:686px;top:202px;width:198px;height:39px">Phone:</div>
  <div class="field" style="left:903px;top:202px;width:197px;height:39px">Email:</div>
  <div class="field" style="left:686px;top:262px;width:414px;height:125px">Mesage:</div>
  <a class="btn btn-blue" style="left:801px;top:424px;width:183px">Submit <svg viewBox="0 0 24 24" fill="none" stroke="currentColor" stroke-width="2"><path d="M4 12h14M12 6l6 6-6 6"/></svg></a>
</section>

<footer class="abs footer">
  <div class="abs" style="left:0;top:70px;width:1200px;display:flex;justify-content:center;align-items:center;gap:18px;font:700 62px Poppins,sans-serif"><span style="width:64px;height:64px;border-radius:50%;background:#fff;display:inline-block"></span>CLEAR RTM</div>
  <div class="abs rule-line" style="top:192px"></div>
  <div class="abs fmenu"><span>CHECK-AND-SETTLE</span><span>PARTNERSHIPS</span><span>INDUSTRIES</span><span>ABOUT</span><span>INDUSTRIES</span><span>CONTACT</span></div>
  <div class="abs rule-line" style="top:268px"></div>
  <div class="abs" style="left:70px;top:290px;display:flex;gap:12px;align-items:center;font-size:13px"><svg width="16" height="16" viewBox="0 0 24 24" fill="none" stroke="#fff" stroke-width="2"><path d="M5 3h4l2 5-3 2a12 12 0 0 0 6 6l2-3 5 2v4a2 2 0 0 1-2 2A17 17 0 0 1 3 5a2 2 0 0 1 2-2z"/></svg>+1 555.010.0199</div>
  <div class="abs" style="right:66px;top:295px;font-size:11px">TERMS OF USE | PRIVACY POLICY</div>
</footer>

</body>
</html>
```